Beauty Salon Industry - Web Design Project

zQuarta is a well-funded start up developing an Online Marketing Platform for small businesses in Europe.
We require a large number of high quality business web designs for our business website builder. Our business websites are seamlessly integrated into our Online Marketing systems and therefore it is important for designers to comply with our Design Guidelines.
This is our second contest and it will focus on the beauty salon industry. We will be running contents every 2-3 weeks for a new industry. Last month, we ran a contest for Builder website designs with 3 top prizes (plus £10 per variation) and we also paid out £25 per design for 20+ entries from designers who did not win the top prizes. So we encourage all entries!
We have included a wire frame this time to encourage you to be as creative as possible with your designs and layout while respecting the following guidelines:
1) You CAN change the layout as much as you like. If you think a vertical menu would look better, then use it. If you think the design would benefit from moving an element to a different location, then you can do that too.
2) You must include ALL the elements in the wire frame in your design.(e.g. latest 2 news entries, a testimonial, 1 gallery image, carousel etc...). Please make sure you have looked through the wire frame and know what is required. Entries that do not include all the elements will not qualify to win.
3) So remember, you CAN change the layout as much as you like but DO NOT remove any elements nor move them to a different page.
4) You may change the size and style of the carousel image. We would like to see as many variations of this as possible.
We are rewarding 3 prizes, and would like the winning designer to design the internal pages to the new design.
As always, if we think your designs could be incorporated into our system, but you do not win the competition, we will reward £25. Therefore, we encourage designers to submit as many designs as possible as we may award up to 25 designs.
Judging criteria : -
1) Visual Design
2) Layout must adhere to best practices and wireframe. If you decide to move elements around significantly please provide reason
3) Functional, informative and drives calls to action
Updates
As usual:
1st place = £350
2nd place = £250
3rd place = £150
Good luck!
Very happy with all the designs submitted so far, and will provide feedback ASAP.
We would like to see you try arranging the elements differently. So please try different navigation types and layouts.
Thanks
Morris
Prize funds for 1st place has been slightly increased.
Thanks
Morris
We have already had some amazing designs submitted. Thanks.
Remember to play with the layout of the elements and try designs with a carousel/slider that is in portrait not just in landscape.
Thanks everyone!
Morris
Hi everyone, we are really enjoying looking through the designs.
We have one NEW requirement. If you have used an image from http://www.frelik-example.com/ in your design, could you please replace it with another.
We are not associated with them.
Thank you.
I have just sent a poll around the office to vote on all the designs and hope to have the results soon.
Good luck and I hope to see all your great designs for our next project in a couple of weeks.
Morris
Hi everyone, we hope you have had a good holiday season. We will be rewarding the prizes very soon, hopefully today or tomorrow.
Thanks
Morris
We are currently going through all the designs that did not win our competition and will be contacting the designers of the designs we would like to use in our system, so please keep an eye on your inbox over the next few days.
Thank you
Morris
Target Market(s)
Beauty Salon Industry
Industry/Entity Type
Beauty Salon
Look and feel
Each slider illustrates characteristics of the customer's brand and the style your logo design should communicate.

```html
<!DOCTYPE html>
<html lang="en">
<head>
<meta charset="utf-8">
<title>Airy Lane – Hair &amp; Urban Spa</title>
<link rel="stylesheet" href="https://fonts.googleapis.com/css2?family=Arimo:wght@400;700&family=Crimson+Text:ital,wght@0,400;0,600;1,400;1,600;1,700&display=swap">
<style>
:root{
  --maroon-dark:#4a0d18;
  --maroon:#6e1526;
  --maroon-mid:#8a2a3a;
  --maroon-light:#a0404f;
  --beige:#e4dccb;
  --cream:#f5f2ea;
  --strip:#efebe2;
  --ink:#4a3a3a;
  --grey:#8a8a8a;
  --white:#ffffff;
  --serif:"Crimson Text", Georgia, serif;
  --sans:"Arimo", Arial, sans-serif;
}
*{margin:0;padding:0;box-sizing:border-box}
html,body{width:1024px;height:1200px;overflow:hidden;background:var(--white)}
.page{position:absolute;left:0;top:0;width:671px;height:786px;transform:scale(1.5261);transform-origin:0 0;font-family:var(--sans);color:var(--grey)}
.abs{position:absolute}

.masthead{left:0;top:0;width:671px;height:290px;background:radial-gradient(ellipse at 50% 0%,var(--maroon-light) 0%,var(--maroon) 45%,var(--maroon-dark) 100%)}
.brand{left:52px;top:8px;color:var(--white)}
.brand-name{font-family:var(--serif);font-size:32px;font-weight:400;line-height:1}
.brand-tag{font-size:9px;letter-spacing:.5px;margin-top:3px;padding-left:2px}
.call{left:522px;top:18px;color:var(--white)}
.call-label{font-size:9px;letter-spacing:.5px}
.call-number{font-size:16px;margin-top:4px}

.nav{left:42px;top:61px;width:586px;height:26px;display:flex;background:linear-gradient(var(--maroon),var(--maroon-dark))}
.nav a{flex:1;display:flex;align-items:center;justify-content:center;color:var(--white);font-size:9.5px;text-decoration:none;border-right:1px solid #7c2535}
.nav a:last-child{border-right:none}
.nav a.active{background:var(--maroon-mid);flex:.8}

.stage{left:42px;top:93px;width:586px;height:189px;background:var(--beige)}
.hero{left:48px;top:99px;width:428px;height:177px;background:linear-gradient(90deg,#6f7a56 0%,#9da382 45%,#c9b7a4 70%,#a89882 100%)}
.hero-caption{left:63px;top:141px;font-family:var(--serif);font-style:italic;font-weight:700;font-size:21px;line-height:21px;color:#1e1e1a}
.dots{left:425px;top:259px;display:flex;gap:5px}
.dots span{width:8px;height:8px;border-radius:50%;background:#8f8f84}
.dots span.on{background:var(--white)}
.tab{left:487px;width:135px;height:20px;font-size:9px;padding:5px 8px;letter-spacing:.2px}
.tab-address{top:99px;background:linear-gradient(var(--white),#e6e2da);color:var(--maroon)}
.tab-hours{top:119px;background:var(--maroon);color:var(--white)}
.tab-hours svg{position:absolute;right:14px;top:8px}
.tab-address svg{position:absolute;right:12px;top:6px}
.hours{left:518px;top:149px;font-size:7.5px;line-height:14.5px;color:var(--grey);list-style:none}

.intro-title{left:48px;top:303px;font-family:var(--serif);font-size:13.5px;letter-spacing:.4px;color:var(--ink)}
.intro-text{left:48px;width:430px;font-size:7.5px;line-height:13px}
.news{left:48px;top:403px;width:428px;height:115px;background:var(--cream);border:1px solid #ddd8cc;box-shadow:0 2px 3px rgba(0,0,0,.08)}
.news-divider{left:261px;top:411px;width:1px;height:95px;background:#ddd8cc}
.news-title{font-family:var(--serif);font-size:11.5px;color:var(--ink);top:411px}
.news-thumb{top:440px;width:46px;height:41px}
.news-text{top:438px;font-size:7.5px;line-height:12px;width:120px}
.more{left:396px;top:502px;font-family:var(--serif);font-style:italic;font-size:8px;color:var(--ink)}

.rule{left:48px;width:428px;height:1px;background:#dcdcdc;box-shadow:0 1px 2px rgba(0,0,0,.12)}
.quote{left:97px;top:549px;width:360px;font-family:var(--serif);font-style:italic;font-size:9.5px;line-height:12px;color:var(--ink)}
.quote-by{left:386px;top:576px;font-size:8.5px;color:var(--maroon)}

.offer{left:487px;top:300px;width:136px;height:160px;background:var(--beige)}
.offer-photo{left:497px;top:311px;width:116px;height:79px;background:linear-gradient(135deg,#e9ddd6,#cfb9ad 60%,#8e5d52)}
.offer-text{left:495px;top:400px;width:75px;font-size:7.5px;line-height:11px;color:#6a6a60}
.offer-price{left:578px;top:398px;font-size:18px;font-weight:700;color:#3a3a34}
.offer-button{left:494px;top:430px;width:121px;height:22px;background:var(--maroon);color:var(--white);font-size:7.8px;font-weight:700;display:flex;align-items:center;justify-content:center;border-radius:2px}
.gallery{left:487px;top:472px;width:136px;height:127px;background:var(--beige);padding:3px}
.gallery div{width:100%;height:100%;background:linear-gradient(160deg,#6a5047,#a98a7d 45%,#2e2421)}
.gallery-link{left:573px;top:601px;font-family:var(--serif);font-style:italic;font-weight:700;font-size:10px;color:var(--maroon)}

.partners{left:0;top:615px;width:671px;height:50px;background:var(--strip)}
.partner{top:631px;width:130px;text-align:center;font-family:var(--serif);font-size:16px;color:#2a2a2a;transform:translateX(-50%)}

.signup{left:0;top:665px;width:671px;height:45px;background:linear-gradient(var(--maroon-mid),var(--maroon))}
.signup-label{left:49px;top:684px;width:138px;white-space:nowrap;font-size:8.3px;font-weight:700;color:var(--white);letter-spacing:-.1px}
.signup-input{left:192px;top:678px;width:178px;height:20px;background:var(--white);font-size:7px;color:#555;padding:6px 6px;white-space:nowrap}
.signup-go{left:370px;top:678px;width:24px;height:20px;background:#2b2b2b;color:var(--white);font-size:8.5px;display:flex;align-items:center;justify-content:center}
.follow{left:525px;top:684px;font-size:8.3px;font-weight:700;color:var(--white);white-space:nowrap}
.follow-dot{top:681px;width:14px;height:14px;border-radius:2px;background:#d9dde6}

.footer{left:0;top:710px;width:671px;height:76px;background:linear-gradient(var(--maroon-dark),#3a0812)}
.footer-links{top:726px;list-style:none;font-size:7.5px;line-height:15px;color:#d9b8bd}
.copyright{left:532px;top:726px;font-size:7.5px;color:#c9a3a9}
</style>
</head>
<body>
<div class="page">
  <header class="abs masthead"></header>
  <div class="abs brand">
    <div class="brand-name">Airy Lane</div>
    <div class="brand-tag">Hair &amp; Urban Spa</div>
  </div>
  <div class="abs call">
    <div class="call-label">CALL US</div>
    <div class="call-number">020 5550 0147</div>
  </div>

  <nav class="abs nav">
    <a class="active" href="#">HOME</a>
    <a href="#">SERVICES</a>
    <a href="#">GALLERY</a>
    <a href="#" style="flex:1.3">TESTIMONIALS</a>
    <a href="#">NEWS</a>
    <a href="#">ABOUT US</a>
    <a href="#">CONTACT US</a>
  </nav>

  <div class="abs stage"></div>
  <div class="abs hero" role="img" aria-label="Carousel photo: woman with long wavy dark hair in an orange dress"></div>
  <div class="abs hero-caption">Lorem ipsum dolor sit<br>amet,&nbsp; sectetuer</div>
  <div class="abs dots"><span class="on"></span><span></span><span></span></div>

  <div class="abs tab tab-address">BLOW ADDRESS
    <svg width="6" height="8" viewBox="0 0 6 8"><path d="M1 1l4 3-4 3" fill="none" stroke="#b7b0a5" stroke-width="1.2"/></svg>
  </div>
  <div class="abs tab tab-hours">BUSINESS HOURS
    <svg width="7" height="4" viewBox="0 0 7 4"><path d="M0 0h7L3.5 4z" fill="#fff"/></svg>
  </div>
  <ul class="abs hours">
    <li>Mon&nbsp; -&nbsp; 9 am - 5 pm</li>
    <li>Tue&nbsp; -&nbsp; 9 am - 5 pm</li>
    <li>wed&nbsp; -&nbsp; 9 am - 5 pm</li>
    <li>Thu&nbsp; -&nbsp; 9 am - 5 pm</li>
    <li>Fri&nbsp; -&nbsp; 9 am - 5 pm</li>
    <li>Sat&nbsp; -&nbsp; 9 am - 5 pm</li>
  </ul>

  <h1 class="abs intro-title">LET OUR HAIR AND BEAUTY SKILLS BLOW YOU AWAY</h1>
  <p class="abs intro-text" style="top:326px">Airy Lane is a passionate, creative team, dedicated to delivering a second to none, personal salon experience that will 'Blow' your mind</p>
  <p class="abs intro-text" style="top:366px">Where ultimate hairdressing comes hand-in-hand with style, glamour, fashion, innovative and skill to create an exquiste salon exprience in the heart og london.</p>

  <section class="abs news"></section>
  <div class="abs news-divider"></div>
  <h2 class="abs news-title" style="left:62px">Book now for Christmas</h2>
  <div class="abs news-thumb" style="left:63px;background:linear-gradient(#3aa7d8,#1f7fb8)" role="img" aria-label="News photo: woman in a festive hat"></div>
  <p class="abs news-text" style="left:120px">Our salon is usually very busy for the two week befor christmas.so please book early:<br>Call 020 5550 0147, or contact us.</p>
  <h2 class="abs news-title" style="left:290px">Want to be hair model?</h2>
  <div class="abs news-thumb" style="left:294px;background:linear-gradient(#8a6a5a,#d8c6b8)" role="img" aria-label="News photo: hair model with a bob cut"></div>
  <p class="abs news-text" style="left:347px">Our salon is usually very busy for the two week befor christmas.so please book early:<br>Call 020 5550 0147, or contact us.</p>
  <div class="abs more">read more news &nbsp;&nbsp;»</div>

  <div class="abs rule" style="top:535px"></div>
  <blockquote class="abs quote">My hairstylist, Marielle, was truly amazing. She listened to exactly what I wanted, but also told me exactly what ......"</blockquote>
  <div class="abs quote-by">- Noreen Pashley</div>
  <div class="abs rule" style="top:600px"></div>

  <aside class="abs offer"></aside>
  <div class="abs offer-photo" role="img" aria-label="Spa photo: client relaxing during a facial treatment"></div>
  <p class="abs offer-text">Comlimentary gift for first - time clients!</p>
  <div class="abs offer-price">$25</div>
  <div class="abs offer-button">BOOK APPOINTMENT NOW</div>
  <div class="abs gallery"><div role="img" aria-label="Gallery photo: stylist working on a client's hair"></div></div>
  <div class="abs gallery-link">View Gallery</div>

  <div class="abs partners"></div>
  <div class="abs partner" style="left:108px">LUMERÉ</div>
  <div class="abs partner" style="left:276px">VELLORA</div>
  <div class="abs partner" style="left:410px">Bramble</div>
  <div class="abs partner" style="left:562px">Stolzhaar</div>

  <div class="abs signup"></div>
  <div class="abs signup-label">SIGN UP FOR OUR NEWLETTER</div>
  <div class="abs signup-input">enter your email address here</div>
  <div class="abs signup-go">GO</div>
  <div class="abs follow">FOLLOW US</div>
  <div class="abs follow-dot" style="left:587px"></div>
  <div class="abs follow-dot" style="left:608px"></div>

  <footer class="abs footer"></footer>
  <ul class="abs footer-links" style="left:47px"><li>Home</li><li>services</li><li>Gallery</li></ul>
  <ul class="abs footer-links" style="left:151px"><li>Testimonials</li><li>News</li><li>About Us</li></ul>
  <div class="abs copyright">© 2011 All Right Reserved</div>
</div>
</body>
</html>
```